Redesign wellness clinic website

The project is redesign a wellness clinic http://www.thornleighvitality.example. The new website is to be responsive,clean,bright and a strong call to action which is to book an appointment. The logo will remain the same but the colour scheme on the website should be reflect purple white and green. I want it to be bright and cheerful and the feeling of clarity. The website shouldn't be overloaded with content but more visuals.

Target Market(s)

Anyone that has corporate wellness benefits within the downtown Toronto core. Majority of audience are professional working in Media, Telecommunications and Investments.

Industry/Entity Type

Health And Wellness

Number of Pages Required

5+ page

Font styles to use
Sans Serif

Colors
ffffff
886aae
acd036

Requirements
Must have
• -Strong call to action which is book an appointment like this page https://www.kestrelmotion.example/
• -Services provided icons on the page like https://www.brightpathvitalityhouse.example/
• - Pictures of a good visualizing a fit and healthy life
• - Strong ratings from Quorva, Zintrel, PostMaz, similar to this website http://www.summitbalancehealth.example/our-team-professionals/
• - Bright and clear
Should not have
• -No black and white images (redo our pictures)
• -Dark themes

```html
<!DOCTYPE html>
<html lang="en">
<head>
<meta charset="utf-8">
<title>Thornleigh Vitality Centre</title>
<link href="https://fonts.googleapis.com/css2?family=Roboto:wght@400;500;700;900&display=swap" rel="stylesheet">
<style>
:root{
  --purple:#886aae;
  --purple-dark:#6f5396;
  --green:#acd036;
  --white:#ffffff;
  --ink:#444444;
  --muted:#777777;
  --dark:#3a3a3a;
  --light:#f4f4f4;
}
*{box-sizing:border-box;margin:0;padding:0}
html,body{width:1200px;height:4762px;overflow:hidden}
body{font-family:"Roboto",Arial,sans-serif;color:var(--ink);background:var(--white);position:relative}
a{color:inherit;text-decoration:none}
.abs{position:absolute}
.btn{display:inline-block;background:var(--purple);color:var(--white);font-weight:700;font-size:15px;text-transform:uppercase;padding:10px 26px;border-radius:3px;letter-spacing:.5px}
.btn-small{font-size:14px;padding:8px 24px;text-transform:none}
.section-title{text-align:center;font-size:36px;font-weight:500;color:var(--ink)}
.section-sub{text-align:center;font-size:15px;color:var(--muted);line-height:1.4;margin-top:8px}

/* top bar */
.topbar{left:0;top:0;width:1200px;height:70px;background:var(--purple)}
.main-nav{display:flex;height:70px;padding-left:80px}
.main-nav a{color:var(--white);font-size:15px;font-weight:700;text-transform:uppercase;padding:0 20px;line-height:70px}
.main-nav a.active{background:var(--purple-dark)}
.call-box{right:0;top:0;height:70px;width:300px;background:var(--dark);display:flex;align-items:center;gap:14px;padding-left:40px;color:var(--white)}
.call-box .lines{font-size:14px;line-height:1.3}
.call-box strong{font-size:18px}

/* logo */
.brand{left:0;top:70px;width:1200px;height:120px;display:flex;flex-direction:column;align-items:center;justify-content:center}
.brand-row{display:flex;align-items:center;gap:12px}
.brand-mark{width:44px;height:44px;border-radius:50%;background:var(--purple)}
.brand-name{font-size:24px;font-weight:700;color:var(--purple)}
.brand-call{font-size:13px;color:var(--green);margin-top:4px;font-weight:500}

/* hero */
.hero{left:0;top:190px;width:1200px;height:493px;background:linear-gradient(120deg,#f7e7b2 0%,#f3c86a 35%,#c69a4a 65%,#8d7a3e 100%)}
.hero-text{left:0;top:190px;width:1200px;height:493px;display:flex;flex-direction:column;align-items:center;justify-content:center;padding-top:90px}
.hero h1{color:var(--white);font-size:34px;font-weight:700;text-align:center;line-height:1.15;letter-spacing:2px;text-shadow:0 1px 4px rgba(0,0,0,.35)}
.hero-text .btn{margin-top:14px}
.hero-arrow{top:410px;width:26px;height:50px;background:rgba(255,255,255,.5)}
.dots{display:flex;gap:8px;justify-content:center}
.dots span{width:10px;height:10px;border-radius:50%;background:#ccc}
.dots span.on{background:var(--green)}

/* services */
.services{left:0;top:740px;width:1200px;height:690px}
.services .section-title{margin-top:20px}
.service-figure{left:476px;top:155px;width:254px;height:455px;border-radius:4px;background:linear-gradient(180deg,#f6f6f6 0%,#e9f0d4 50%,#cfe293 100%)}
.service{width:300px;text-align:center}
.service .icon{display:block;margin:0 auto 6px}
.service h3{font-size:15px;color:var(--purple);font-weight:500}
.service p{font-size:13px;color:var(--muted);line-height:1.35;margin-top:4px}
.service .more{font-size:12px;color:var(--purple);margin-top:4px;display:block}
.services .btn{left:548px;top:625px}

/* join */
.join{left:0;top:1429px;width:1200px;height:565px;background:linear-gradient(110deg,#cfc7bd 0%,#e9dfd4 40%,#d6b9a0 70%,#b79a84 100%)}
.join-box{left:41px;top:89px;width:500px;height:355px;background:var(--green);opacity:.95;padding:40px 44px;color:var(--white)}
.join-box h2{font-size:28px;font-weight:500;margin-bottom:16px}
.join-box p{font-size:15px;font-weight:700;line-height:1.35;margin-bottom:14px}
.join-box .btn{background:var(--purple);font-size:14px;text-transform:none;padding:8px 20px;margin-top:4px}

/* staff */
.staff{left:0;top:2080px;width:1200px;height:640px}
.tabs{display:flex;justify-content:center;margin-top:16px}
.tabs span{background:var(--green);color:var(--white);font-size:13px;font-weight:700;padding:6px 12px;border-right:1px solid rgba(255,255,255,.6)}
.tabs span.on{background:var(--purple)}
.staff-cards{left:60px;top:142px;width:1080px;display:flex;justify-content:space-between}
.staff-card{width:250px;height:302px;text-align:center;padding-top:14px}
.staff-card.featured{box-shadow:0 0 10px rgba(0,0,0,.15)}
.avatar{width:200px;height:200px;border-radius:50%;margin:0 auto;border:4px solid var(--green);background:radial-gradient(circle at 50% 40%,#d8d8d8,#9a9a9a)}
.staff-card h4{font-size:14px;color:var(--purple);font-weight:700;text-transform:uppercase;margin-top:12px}
.staff-card .role{font-size:13px;color:var(--muted);line-height:1.3;margin-top:4px;min-height:34px}
.staff-card .contact{font-size:13px;color:var(--ink);margin-top:8px}
.staff-card .social{font-size:10px;color:#aaa;margin-top:4px}
.side-arrow{top:2320px;width:22px;height:54px;background:#ddd}
.staff .dots{position:absolute;left:0;top:590px;width:1200px}

/* news */
.news{left:0;top:2756px;width:1200px;height:657px;background:var(--purple);color:var(--white)}
.news .section-title{color:var(--white);margin-top:56px}
.news .section-sub{color:var(--white);font-weight:700}
.news-cards{left:80px;top:146px;width:1040px;display:flex;justify-content:space-between}
.news-card{width:334px;height:386px;background:var(--white);border:4px solid var(--white);color:var(--ink)}
.news-photo{height:192px;background:linear-gradient(135deg,#f2f2f2,#c9c3cf 60%,#9d95a6)}
.news-body{padding:10px 14px}
.news-body h4{font-size:14px;font-weight:700;line-height:1.3}
.news-meta{display:flex;justify-content:space-between;font-size:11px;color:var(--purple);margin-top:6px}
.news-body p{font-size:12px;line-height:1.35;color:var(--muted);margin-top:6px}
.news-body .more{font-size:12px;color:var(--purple);display:block;margin-top:8px}
.news .btn{left:552px;top:574px;background:var(--white);color:var(--purple)}

/* testimonial */
.parents{left:0;top:3413px;width:1200px;height:640px}
.parents .section-title{margin-top:50px;font-weight:700}
.quote-avatar{left:500px;top:125px;width:200px;height:200px;border-radius:50%;background:radial-gradient(circle at 50% 40%,#f0e4dc,#c9b2a3);border:6px solid #eee}
.quote{left:250px;top:340px;width:700px;text-align:center}
.quote h4{font-size:20px;font-weight:500}
.quote .title{font-size:13px;color:var(--muted);margin-top:2px}
.quote p{font-size:15px;line-height:1.4;margin-top:14px}
.quote .more{font-size:13px;color:var(--purple);display:block;margin-top:10px}
.parents .dots{position:absolute;left:0;top:520px;width:1200px}
.parents .btn{left:536px;top:545px}

/* newsletter */
.newsletter{left:0;top:4080px;width:1200px;height:238px;background:var(--green);color:var(--white);text-align:center}
.newsletter h2{font-size:26px;font-weight:700;margin-top:58px;letter-spacing:.5px}
.newsletter .lead{font-size:15px;font-weight:700;margin-top:4px}
.subscribe{display:flex;justify-content:center;margin-top:24px}
.subscribe span{width:460px;height:38px;background:var(--white);border-radius:20px 0 0 20px;text-align:left;padding:10px 18px;color:#999;font-size:14px}
.subscribe b{width:130px;height:38px;background:var(--purple);color:var(--white);font-size:15px;line-height:38px;border-radius:0 20px 20px 0}

/* footer */
.footer{left:0;top:4343px;width:1200px;height:372px;background:var(--purple);color:var(--white)}
.foot-col{top:62px}
.foot-col h5{font-size:15px;font-weight:700;text-transform:uppercase;margin-bottom:14px}
.foot-col p,.foot-col li{font-size:14px;line-height:1.5;font-weight:500}
.foot-col ul{list-style:none}
.foot-col ul.links li::before{content:"";display:inline-block;width:7px;height:7px;border-radius:50%;background:var(--white);margin-right:10px;vertical-align:middle}
.contact-row{display:flex;gap:10px;align-items:flex-start}
.contact-row svg{flex:none;margin-top:3px}
.socials{display:flex;gap:10px;margin-top:8px}
.socials span{width:28px;height:28px;border-radius:50%;background:var(--white);opacity:.85}
.bottombar{left:0;top:4715px;width:1200px;height:47px;background:var(--dark);color:var(--white);font-size:13px;line-height:47px;padding-left:80px}
</style>
</head>
<body>

<header class="abs topbar">
  <nav class="main-nav">
    <a class="active" href="#">Home</a><a href="#">Services</a><a href="#">Staff</a><a href="#">News</a><a href="#">Corporate Wellness</a><a href="#">Forms</a><a href="#">Contact</a>
  </nav>
</header>
<div class="abs call-box">
  <svg width="26" height="26" viewBox="0 0 24 24"><path fill="#fff" d="M6.6 10.8a15 15 0 0 0 6.6 6.6l2.2-2.2a1 1 0 0 1 1-.25 11.4 11.4 0 0 0 3.6.57 1 1 0 0 1 1 1V20a1 1 0 0 1-1 1A17 17 0 0 1 3 4a1 1 0 0 1 1-1h3.5a1 1 0 0 1 1 1c0 1.25.2 2.45.57 3.57a1 1 0 0 1-.25 1z"/></svg>
  <div class="lines">Call us Now 24/7<br><strong>416-555-0142</strong></div>
</div>

<div class="abs brand">
  <div class="brand-row"><span class="brand-mark"></span><span class="brand-name">Thornleigh Vitality Centre</span></div>
  <div class="brand-call">Call 416-555-0142</div>
</div>

<section class="abs hero" role="img" aria-label="Photo of a woman with arms spread in a sunlit summer field"></section>
<div class="abs hero-text hero">
  <h1>MANY DISCIPLINES<br>ONE PHILOSOPHY</h1>
  <a class="btn" href="#">Book Now</a>
</div>
<div class="abs hero-arrow" style="left:0"></div>
<div class="abs dots" style="left:0;top:713px;width:1200px"><span class="on"></span><span></span><span></span></div>

<section class="abs services">
  <h2 class="section-title">Our Services</h2>
  <p class="section-sub">Lorem Ipsum is simply dummy text of the printing industry ipsum has<br>ever the text ever the industry's</p>
  <div class="abs service-figure" role="img" aria-label="Photo of a smiling woman sitting cross-legged holding vegetables and a dumbbell"></div>

  <div class="abs service" style="left:168px;top:158px">
    <svg class="icon" width="44" height="36" role="img" aria-label="Chiropractic table icon"><circle cx="22" cy="18" r="16" fill="none" stroke="#886aae" stroke-width="2"/></svg>
    <h3>Chiropractic</h3><p>Lorem Ipsum is simply dummy<br>text ever the industry's</p><span class="more">Read More.. »</span>
  </div>
  <div class="abs service" style="left:708px;top:158px">
    <svg class="icon" width="44" height="36" role="img" aria-label="Physiotherapy figure icon"><circle cx="22" cy="18" r="16" fill="none" stroke="#886aae" stroke-width="2"/></svg>
    <h3>Physiotherapy</h3><p>Lorem Ipsum is simply dummy<br>text ever the industry's</p><span class="more">Read More.. »</span>
  </div>
  <div class="abs service" style="left:88px;top:335px">
    <svg class="icon" width="44" height="36" role="img" aria-label="Massage therapy icon"><circle cx="22" cy="18" r="16" fill="none" stroke="#886aae" stroke-width="2"/></svg>
    <h3>Massage Therapy</h3><p>Lorem Ipsum simply dummy<br>ever the industry's</p><span class="more">Read More.. »</span>
  </div>
  <div class="abs service" style="left:802px;top:335px">
    <svg class="icon" width="44" height="36" role="img" aria-label="Nutrition apple icon"><circle cx="22" cy="18" r="16" fill="none" stroke="#886aae" stroke-width="2"/></svg>
    <h3>Nutrition and Lifestyle Medicine</h3><p>Lorem Ipsum simply dummy<br>ever the industry's</p><span class="more">Read More.. »</span>
  </div>
  <div class="abs service" style="left:183px;top:520px">
    <svg class="icon" width="44" height="36" role="img" aria-label="Active rehabilitation icon"><circle cx="22" cy="18" r="16" fill="none" stroke="#886aae" stroke-width="2"/></svg>
    <h3>Active Rehabilitation</h3><p>Lorem Ipsum simply dummy text<br>ever the industry's</p><span class="more">Read More.. »</span>
  </div>
  <div class="abs service" style="left:739px;top:520px">
    <svg class="icon" width="44" height="36" role="img" aria-label="Osteopathy icon"><circle cx="22" cy="18" r="16" fill="none" stroke="#886aae" stroke-width="2"/></svg>
    <h3>Osteopathy</h3><p>Lorem Ipsum simply dummy<br>ever the industry's</p><span class="more">Read More.. »</span>
  </div>
  <a class="abs btn btn-small" href="#">View More</a>
</section>

<section class="abs join" role="img" aria-label="Photo of a therapist treating a patient's shoulder"></section>
<div class="abs join-box" style="top:1518px">
  <h2>Come and join our Family</h2>
  <p>Our Centre is committed to helping improve and extend the lives of as many people as possible in our community.</p>
  <p>Come and join our Family and start changing your life today.</p>
  <p>Planning a wellness fair? We can help! Contact us at info@thornleighvitality.example for more details.</p>
  <a class="btn" href="#">Read More</a>
</div>

<section class="abs staff">
  <h2 class="section-title">Staff</h2>
  <p class="section-sub" style="margin-top:4px">Lorem Ipsum is simply dummy text of the printing industry ever the industry's</p>
  <div class="tabs"><span class="on">Chiropractic</span><span>Physiotherapy</span><span>Active Rehabilitation</span><span>Massage Therapy</span><span>Nutrition and Lifestyle Medicine</span><span>Chiropody</span><span>Osteopathy</span></div>
  <div class="abs staff-cards">
    <div class="staff-card"><div class="avatar" role="img" aria-label="Staff portrait photo"></div><h4>Dr. Colin Varga</h4><p class="role">Chiropractor, Director<br>of Clinic</p><p class="contact">Contact Me</p><p class="social">Profile · Bio · Book</p></div>
    <div class="staff-card featured"><div class="avatar" role="img" aria-label="Staff portrait photo"></div><h4>Dr. Nathan Lio</h4><p class="role">Chiropractor</p><p class="contact">Contact Me</p><p class="social">Profile · Bio · Book</p></div>
    <div class="staff-card"><div class="avatar" role="img" aria-label="Staff portrait photo"></div><h4>Dr. Elias Marrow</h4><p class="role">Chiropractor, Functional<br>Chiropractor</p><p class="contact">Contact Me</p><p class="social">Profile · Bio · Book</p></div>
    <div class="staff-card"><div class="avatar" role="img" aria-label="Staff portrait photo"></div><h4 style="text-transform:none">Owen Pardo</h4><p class="role" style="color:var(--ink);font-weight:700">Chiropractor, Functional<br>Chiropractor</p><p class="contact" style="font-weight:700">Contact Me</p><p class="social">Profile · Bio · Book</p></div>
  </div>
  <div class="dots"><span class="on"></span><span></span><span></span></div>
</section>
<div class="abs side-arrow" style="left:0"></div>
<div class="abs side-arrow" style="right:0"></div>

<section class="abs news">
  <h2 class="section-title">Latest News</h2>
  <p class="section-sub">Lorem Ipsum is simply dummy text of the printing industry ipsum has<br>ever the text ever the industry's</p>
  <div class="abs news-cards">
    <article class="news-card"><div class="news-photo" role="img" aria-label="Photo of a woman exercising with a fitness ball"></div><div class="news-body"><h4>6 Ways Physiotherapy can help relieve Aches and Pains</h4><div class="news-meta"><span>Dec 6th, 2017</span><span>by Doctor Renn</span></div><p>Physiotherapy is a healthcare service that enhances the quality of life of individuals through alleviating aches and pain and improving movement and function.</p><span class="more">Read More.. »</span></div></article>
    <article class="news-card"><div class="news-photo" role="img" aria-label="Photo of a patient training on rehabilitation equipment"></div><div class="news-body"><h4>6 Ways Physiotherapy can help relieve Aches and Pains</h4><div class="news-meta"><span>Dec 6th, 2017</span><span>by Doctor Renn</span></div><p>Physiotherapy is a healthcare service that enhances the quality of life of individuals through alleviating aches and pain and improving movement and function.</p><span class="more">Read More.. »</span></div></article>
    <article class="news-card"><div class="news-photo" role="img" aria-label="Photo of a therapist assisting a patient's arm"></div><div class="news-body"><h4>6 Ways Physiotherapy can help relieve Aches and Pains</h4><div class="news-meta"><span>Dec 6th, 2017</span><span>by Doctor Renn</span></div><p>Physiotherapy is a healthcare service that enhances the quality of life of individuals through alleviating aches and pain and improving movement and function.</p><span class="more">Read More.. »</span></div></article>
  </div>
  <a class="abs btn btn-small" href="#">View More</a>
</section>

<section class="abs parents">
  <h2 class="section-title">PARENTS SAYS</h2>
  <p class="section-sub" style="margin-top:4px">Lorem Ipsum is simply dummy text of the printing and industry.</p>
  <div class="abs quote-avatar" role="img" aria-label="Portrait photo of the reviewer"></div>
  <div class="abs quote">
    <h4>Maren Ashby</h4><p class="title">Creative Director</p>
    <p>Lorem Ipsum is simply dummy text of the printing and typesetting industry. the industry's standard dummy text ever since the 1500s,when an unknown printer took a galley of type and scrambled</p>
    <span class="more">Read More.. »</span>
  </div>
  <div class="dots"><span class="on"></span><span></span><span></span></div>
  <a class="abs btn btn-small" href="#">View More</a>
</section>

<section class="abs newsletter">
  <h2>SUBSCRIBE TO OUR NEWSLETTER</h2>
  <p class="lead">To Receive The Latest News And Update</p>
  <div class="subscribe"><span>Your E-Mail</span><b>SUBMIT</b></div>
</section>

<footer class="abs footer">
  <div class="abs foot-col" style="left:80px;width:250px">
    <div class="brand-row" style="margin-bottom:14px"><span class="brand-mark" style="background:#fff;width:34px;height:34px"></span><span style="font-size:20px;font-weight:700">Thornleigh</span></div>
    <p>Established in 1989 the Thornleigh Vitality Centre has become one of Canada's leaders in providing quality care and innovative wellness programs.</p>
    <p style="margin-top:10px">Read More.. »</p>
  </div>
  <div class="abs foot-col" style="left:375px">
    <h5>Quick Link</h5>
    <ul class="links"><li>Home</li><li>Services</li><li>Staff</li><li>News</li><li>Corporate</li><li>Forms</li><li>Contact</li></ul>
  </div>
  <div class="abs foot-col" style="left:556px;width:250px">
    <h5>Contact Us</h5>
    <div class="contact-row"><svg width="14" height="18" viewBox="0 0 14 18"><path fill="#fff" d="M7 0a7 7 0 0 0-7 7c0 5 7 11 7 11s7-6 7-11a7 7 0 0 0-7-7zm0 9.5A2.5 2.5 0 1 1 7 4.5a2.5 2.5 0 0 1 0 5z"/></svg><p>Thornleigh Vitality Centre<br>48 Alderbank Avenue,<br>Suite 210 Toronto, Ontario<br>M5X 0A9</p></div>
    <div class="contact-row"><svg width="14" height="14" viewBox="0 0 24 24"><path fill="#fff" d="M6.6 10.8a15 15 0 0 0 6.6 6.6l2.2-2.2a1 1 0 0 1 1-.25 11.4 11.4 0 0 0 3.6.57 1 1 0 0 1 1 1V20a1 1 0 0 1-1 1A17 17 0 0 1 3 4a1 1 0 0 1 1-1h3.5a1 1 0 0 1 1 1c0 1.25.2 2.45.57 3.57a1 1 0 0 1-.25 1z"/></svg><p>416-555-0142</p></div>
    <div class="contact-row"><svg width="14" height="14" viewBox="0 0 14 14"><rect x="1" y="3" width="12" height="9" fill="none" stroke="#fff" stroke-width="1.6"/><rect x="3" y="1" width="8" height="3" fill="#fff"/></svg><p>Fax: 416-555-0187</p></div>
    <div class="contact-row"><svg width="14" height="14" viewBox="0 0 14 14"><rect x="1" y="3" width="12" height="9" fill="none" stroke="#fff" stroke-width="1.6"/><path d="M1 3l6 5 6-5" fill="none" stroke="#fff" stroke-width="1.6"/></svg><p>info@thornleighvitality.example</p></div>
  </div>
  <div class="abs foot-col" style="left:835px;width:290px">
    <h5>Hours of Operation</h5>
    <p>Monday - Friday 7:30am - 8pm<br>Saturday 10am - 5pm<br>Sunday 10am - 5pm</p>
    <h5 style="margin-top:18px;margin-bottom:4px">Follow Us</h5>
    <div class="socials"><span></span><span></span><span></span><span></span><span></span></div>
  </div>
</footer>
<div class="abs bottombar">Copy Right ©2017 All Rights Reserved.</div>

</body>
</html>
```